Digital Ad for Savor Parade Valentine's Special Event

Savor Parade is producing a special Valentine's all-inclusive food and beverage +21 tasting event on Saturday February 11, 2023 at the Bluecrest Hangar Gallery in Dallas, TX. We looking for a final push on ticket sales with a digital campaign targeting higher demo meen with this different valentine option then then traditional going out to dinner. And with the Grand Clash on Sunday Feb 12th, maybe there in an angle on making is a Super Weekend or something.

Title – Max length 50 characters
Image type – jpg, jpeg, gif, png
Image size - 300x250, 300x600
Max image size – 100kb
Description Max Length – 160 characters
Call-To-Action button copy max length – 15 characters

```html
<!DOCTYPE html>
<html lang="en">
<head>
<meta charset="utf-8">
<title>Savor Parade Valentine's Special Event – Digital Ads</title>
<link rel="stylesheet" href="https://fonts.googleapis.com/css2?family=Montserrat:wght@400;500;700&family=Raleway:wght@400;700;800&display=swap">
<style>
  :root {
    --stage: #3b3b3b;
    --plum: #5a1462;
    --berry: #8a1450;
    --crimson: #b3121f;
    --deep-red: #9c0d18;
    --white: #ffffff;
    --cream: #fbe7b4;
    --lemon: #e3e80b;
    --band: rgba(70, 0, 20, 0.18);
  }
  * { box-sizing: border-box; margin: 0; padding: 0; }
  html, body { width: 1200px; height: 1120px; overflow: hidden; }
  body {
    background: var(--stage);
    position: relative;
    font-family: "Montserrat", Arial, sans-serif;
    color: var(--white);
  }
  .ad {
    position: absolute;
    width: 300px;
    overflow: hidden;
    transform-origin: 0 0;
    transform: scale(1.607);
    background: linear-gradient(180deg, var(--plum) 0%, var(--berry) 38%, var(--crimson) 78%, var(--deep-red) 100%);
    box-shadow: 0 3px 10px rgba(0,0,0,0.45);
    text-align: center;
  }
  .ad--skyscraper { left: 92px; top: 84px; height: 600px; }
  .ad--rectangle { left: 629px; top: 388px; height: 250px; }

  .ad .line { position: absolute; left: 0; right: 0; white-space: nowrap; }
  .band { position: absolute; left: 0; right: 0; background: var(--band); }

  .brand-name {
    font-family: "Raleway", Arial, sans-serif;
    font-weight: 800;
    color: var(--white);
    letter-spacing: 1px;
    line-height: 1.08;
  }
  .valentines {
    font-family: "Raleway", Arial, sans-serif; font-weight: 800;
    color: var(--cream); letter-spacing: 1px; line-height: 1;
    text-shadow: 1px 2px 0 rgba(60,0,30,0.55);
  }
  .special { font-family: "Raleway", Arial, sans-serif; font-weight: 400; letter-spacing: 3px; line-height: 1; }
  .date { font-weight: 700; line-height: 1.15; }
  .highlight { color: var(--lemon); }
  .venue { line-height: 1.35; }
  .venue strong { font-weight: 700; }
  .details { font-weight: 400; line-height: 1.45; }
  .details strong { font-weight: 700; }

  /* 300x600 */
  .ad--skyscraper .brand-name { top: 50px; font-size: 40px; }
  .ad--skyscraper .valentines { top: 150px; font-size: 26px; }
  .ad--skyscraper .special { top: 183px; font-size: 17px; }
  .ad--skyscraper .band--date { top: 243px; height: 120px; }
  .ad--skyscraper .date { top: 253px; font-size: 28px; }
  .ad--skyscraper .venue { top: 388px; font-size: 17px; }
  .ad--skyscraper .venue .at { font-size: 18px; font-weight: 400; }
  .ad--skyscraper .band--details { top: 485px; height: 83px; }
  .ad--skyscraper .details { top: 491px; font-size: 12.5px; }

  /* 300x250 */
  .ad--rectangle .brand-name { top: 20px; font-size: 30px; line-height: 1.05; }
  .ad--rectangle .valentines { top: 95px; font-size: 21px; }
  .ad--rectangle .special { top: 120px; font-size: 13px; }
  .ad--rectangle .band--date { top: 140px; height: 45px; }
  .ad--rectangle .date { top: 150px; font-size: 14px; }
  .ad--rectangle .venue { top: 168px; font-size: 9.5px; }
  .ad--rectangle .band--details { top: 186px; height: 64px; }
  .ad--rectangle .details { top: 194px; font-size: 10px; line-height: 1.4; }
</style>
</head>
<body>

<section class="ad ad--skyscraper" aria-label="Savor Parade Valentine's ad, 300 by 600">
  <div class="band band--date"></div>
  <div class="band band--details"></div>
  <h1 class="line brand-name">SAVOR<br>PARADE</h1>
  <p class="line valentines">VALENTINE'S</p>
  <p class="line special">SPECIAL EVENT</p>
  <p class="line date">SATURDAY<br><span class="highlight">FEBRUARY 11</span><br>2023</p>
  <p class="line venue"><span class="at">At the</span><br><strong>Bluecrest Hangar Gallery</strong><br><strong>in Dallas, TX</strong></p>
  <p class="line details">all-inclusive food and beverage<br>+21 tasting event and<br>with the Grand Clash on<br><strong>SUNDAY FEB 12TH</strong></p>
</section>

<section class="ad ad--rectangle" aria-label="Savor Parade Valentine's ad, 300 by 250">
  <div class="band band--date"></div>
  <div class="band band--details"></div>
  <h1 class="line brand-name">SAVOR<br>PARADE</h1>
  <p class="line valentines">VALENTINE'S</p>
  <p class="line special">SPECIAL EVENT</p>
  <p class="line date">SATURDAY <span class="highlight">FEBRUARY 11</span>, 2023</p>
  <p class="line venue">at the Bluecrest Hangar Gallery in Dallas, TX</p>
  <p class="line details">all-inclusive food and beverage<br>+21 tasting event and with the Grand Clash on<br><strong>SUNDAY FEB 12TH</strong></p>
</section>

</body>
</html>
```